business stationery for email layout
startup company
Simple
RT
Via G. Morelli, 17
26813 Codogno LO
Italy
Info@Tallimora.com
www.tallimora.com
minimalist, retail, fashion, technology, internet, innovative,one-step ahead, easy, intuitive, immediate, serious,credible
logo blue version
logo grey version
symbol blue version
symbol grey version

```html
<!DOCTYPE html>
<html lang="it">
<head>
<meta charset="utf-8">
<title>Tallimora – Business Card</title>
<link href="https://fonts.googleapis.com/css2?family=Open+Sans:wght@400;700;800&display=swap" rel="stylesheet">
<style>
  :root {
    --backdrop: #e6e7ea;
    --card: #ffffff;
    --band-dark: #1e2f8f;
    --band-light: #3a5cc4;
    --accent-line: #7fcbe6;
    --brand: #1f2f86;
    --text: #555a63;
    --divider: #c9ccd2;
    --icon: #3a4a9a;
  }
  * { margin: 0; padding: 0; box-sizing: border-box; }
  html, body {
    width: 1200px; height: 780px; overflow: hidden;
    background: var(--backdrop);
    font-family: "Open Sans", Arial, sans-serif;
  }
  .card {
    position: absolute; left: 100px; top: 90px;
    width: 1000px; height: 600px;
    background: var(--card);
    border-radius: 36px;
    overflow: hidden;
    box-shadow: 0 12px 30px rgba(0,0,0,0.18);
  }
  .card__band { position: absolute; left: 0; top: 0; width: 1000px; height: 220px; }
  .card__initials {
    position: absolute; right: 54px; top: 34px;
    color: #fff; font-weight: 700; font-size: 40px; letter-spacing: 1px;
  }
  .brand {
    position: absolute; left: 150px; top: 228px;
    display: flex; align-items: center; gap: 18px;
  }
  .brand__dot { width: 26px; height: 26px; border-radius: 50%; background: var(--brand); }
  .brand__name {
    font-weight: 800; font-size: 86px; color: var(--brand);
    letter-spacing: 1px; text-transform: uppercase; line-height: 1;
  }
  .address {
    position: absolute; right: 520px; top: 430px;
    text-align: right; color: var(--text); font-size: 24px; line-height: 36px;
  }
  .divider {
    position: absolute; left: 500px; top: 400px;
    width: 2px; height: 165px; background: var(--divider);
  }
  .contacts {
    position: absolute; left: 530px; top: 398px;
    list-style: none; color: var(--text); font-size: 22px;
  }
  .contacts li { display: flex; align-items: center; gap: 14px; height: 42px; }
  .contacts svg { width: 22px; height: 22px; flex: none; }
</style>
</head>
<body>
  <main class="card">
    <svg class="card__band" viewBox="0 0 1000 220" aria-hidden="true">
      <defs>
        <linearGradient id="bandFill" x1="0" y1="0" x2="1" y2="1">
          <stop offset="0" stop-color="var(--band-dark)"/>
          <stop offset="1" stop-color="var(--band-light)"/>
        </linearGradient>
      </defs>
      <path d="M0 0 H1000 V118 Q620 205 0 172 Z" fill="url(#bandFill)"/>
      <path d="M0 186 Q620 220 1000 132" fill="none" stroke="var(--accent-line)" stroke-width="8"/>
    </svg>
    <div class="card__initials">RT</div>

    <div class="brand">
      <span class="brand__dot"></span>
      <span class="brand__name">Tallimora</span>
    </div>

    <address class="address">
      Via G. Morelli, 17<br>
      26813 Codogno LO, Italy
    </address>

    <div class="divider"></div>

    <ul class="contacts">
      <li>
        <svg viewBox="0 0 24 24"><path fill="var(--icon)" d="M6.6 10.8a15 15 0 0 0 6.6 6.6l2.2-2.2a1 1 0 0 1 1-.25 11.4 11.4 0 0 0 3.6.57 1 1 0 0 1 1 1V20a1 1 0 0 1-1 1A17 17 0 0 1 3 4a1 1 0 0 1 1-1h3.5a1 1 0 0 1 1 1c0 1.25.2 2.45.57 3.57a1 1 0 0 1-.25 1z"/></svg>
        +390245081126
      </li>
      <li>
        <svg viewBox="0 0 24 24"><g fill="var(--icon)"><rect x="6" y="3" width="12" height="6" rx="1"/><rect x="2" y="9" width="20" height="9" rx="2"/><rect x="6" y="15" width="12" height="6" fill="#fff" stroke="var(--icon)" stroke-width="2"/></g></svg>
        +390245081190
      </li>
      <li>
        <svg viewBox="0 0 24 24"><circle cx="12" cy="12" r="4" fill="none" stroke="var(--icon)" stroke-width="2.4"/><path d="M16 8v5.5a2.5 2.5 0 0 0 5 0V12a9 9 0 1 0-3.5 7.1" fill="none" stroke="var(--icon)" stroke-width="2.4"/></svg>
        Info@Tallimora.com
      </li>
      <li>
        <svg viewBox="0 0 24 24"><g fill="none" stroke="var(--icon)" stroke-width="2"><circle cx="12" cy="12" r="9.5"/><ellipse cx="12" cy="12" rx="4" ry="9.5"/><path d="M2.5 12h19M4 7h16M4 17h16"/></g></svg>
        www.tallimora.com
      </li>
    </ul>
  </main>
</body>
</html>
```